Awesome Web Design Project

must have a link to mingleton of the homepage preferably a scrolling view of our mingleton page!

We are an exciting new electrical company with a strong focus on energy efficiency and offering the latest technologies.

The design should allow easy navigation, there shouldn't be too many menus, It should look clean and sleek, Colours to consider could be green, silver/chrome, black,

The site should convey technology, efficiency and simplicity

Must be viewable on all devices, pc's, tablets, phones ie Responsive
Updates

Logo and some pics uploaded!

Industry/Entity Type

Electrical

Requirements
Must have
• must include the following pages,
about us
our services
gallery
contact us
Connect with us
Nice to have
• Would be great if the website design used a user friendly cms,
Should not have
• too many links, menus, clutter it should be clean and easy to navigate

```html
<!DOCTYPE html>
<html lang="en">
<head>
<meta charset="utf-8">
<title>Volten Electrical</title>
<link rel="stylesheet" href="https://fonts.googleapis.com/css2?family=Audiowide&family=Oswald:wght@300;400;600&display=swap">
<style>
:root{
  --ink:#0c2e35;
  --teal:#0b2d33;
  --lime:#d6e021;
  --olive:#a8a300;
  --green:#5c9a0b;
  --footer:#3e5f66;
  --field:#5f858c;
  --muted:#c9d6d8;
  --text:#1b1b1b;
}
*{margin:0;padding:0;box-sizing:border-box}
html,body{width:796px;height:1200px;overflow:hidden;background:#fff}
body{font-family:Arial,Helvetica,sans-serif;color:var(--text);position:relative}
.display{font-family:'Audiowide',sans-serif}
.cond{font-family:'Oswald',sans-serif}

.site-header{height:60px;position:relative;border-bottom:3px solid var(--olive)}
.brand{position:absolute;left:15px;top:15px;display:flex;align-items:center;gap:8px}
.brand-mark{width:26px;height:26px;background:var(--lime)}
.brand-name{font-family:'Audiowide',sans-serif;font-size:19px;color:var(--ink);letter-spacing:2px;line-height:1}
.social-top{position:absolute;right:14px;top:9px;display:flex;align-items:center;gap:6px}
.social-top p{font-family:'Oswald',sans-serif;font-size:13px;line-height:14px;color:var(--ink);text-align:right}
.social-top p b{font-weight:600}
.social-top .sq{width:40px;height:40px;background:#5d7479;border-radius:4px}

.main-nav{height:35px;background:var(--teal);display:flex;justify-content:space-around;align-items:center;padding:0 8px}
.main-nav a{font-family:'Audiowide',sans-serif;color:var(--lime);font-size:13px;letter-spacing:1.5px;text-decoration:none;text-transform:uppercase}

.hero{height:315px;position:relative;background:linear-gradient(100deg,#3d5a78 0%,#c9c9c2 35%,#e5e3da 52%,#a9aaa4 62%,#3f5c7a 80%,#2e4863 100%)}
.dots{position:absolute;right:14px;bottom:10px;display:flex;gap:11px}
.dots span{width:16px;height:16px;border-radius:50%;background:var(--lime)}
.fade{height:42px;background:linear-gradient(#e0e0e0,#fff)}

.content{display:flex;padding:0 15px}
.primary{width:505px}
.aside{margin-left:77px;width:185px}
h1{font-family:'Audiowide',sans-serif;font-weight:400;font-size:25px;color:var(--ink);letter-spacing:2px;margin-top:18px}
.intro{font-size:11.6px;line-height:13.8px;margin-top:13px}
h2{font-family:'Audiowide',sans-serif;font-weight:400;font-size:14.5px;color:var(--ink);letter-spacing:1.5px;margin-top:20px}
.energy{display:flex;margin-top:10px}
.energy .art{width:240px;height:155px;background:radial-gradient(circle at 45% 50%,#eaf6c8,#b9dc5c 45%,#fff 75%);flex:none}
.energy .copy{margin-left:13px;font-size:11.6px;line-height:13.8px}
.energy ul{list-style:none;margin-top:12px}
.energy li{color:var(--green);padding-left:13px;position:relative}
.energy li::before{content:"";position:absolute;left:0;top:4px;width:7px;height:7px;border-radius:50%;background:var(--ink)}
h3{font-family:'Oswald',sans-serif;font-weight:600;font-size:21px;color:var(--ink);margin-top:46px;letter-spacing:-.3px}
.services{display:flex;gap:22px;margin-top:16px}
.services span{background:var(--lime);border-radius:6px;font-family:'Oswald',sans-serif;font-size:16px;color:var(--ink);padding:6px 14px}

.aside h4{font-family:'Oswald',sans-serif;font-weight:300;font-size:26px;color:var(--ink);margin-top:12px}
.quote{margin-top:10px;font-size:9.6px;line-height:12px;border-bottom:1px dotted var(--olive);padding-bottom:14px;margin-bottom:14px}
.quote .bubble{float:left;width:40px;height:28px;margin-right:8px;margin-bottom:2px}
.quote cite{display:block;font-style:normal;color:var(--green);font-size:11.5px;margin-top:12px}
.call{display:flex;align-items:center;gap:6px;font-family:'Oswald',sans-serif;font-weight:300;font-size:20px;color:var(--ink);margin-top:12px}
.phone-big{font-family:'Oswald',sans-serif;font-weight:300;font-size:34px;color:var(--ink);line-height:1}

.site-footer{position:absolute;left:0;top:950px;width:796px;height:250px;background:var(--footer);display:flex;padding:28px 0 0 26px}
.site-footer h5{font-family:'Oswald',sans-serif;font-weight:300;font-size:16px;color:var(--lime);margin-bottom:10px}
.fcol-nav{width:122px;border-right:1px dotted #5f7c82;height:190px}
.fcol-nav a{display:block;color:var(--muted);font-size:10px;line-height:12px;text-decoration:none}
.fcol-mail{margin-left:74px;width:246px}
.field{background:var(--field);border-radius:11px;height:21px;color:#dfe8e9;font-size:8.5px;font-weight:bold;padding:6px 15px;margin-bottom:5px}
.field.area{height:83px;border-radius:12px}
.send{display:block;margin:9px 2px 0 auto;width:56px;height:24px;background:var(--lime);border-radius:3px;font-size:9.5px;font-weight:bold;color:var(--ink);text-align:center;line-height:24px}
.fcol-connect{margin-left:71px;border-left:1px dotted #5f7c82;padding-left:78px;height:190px;width:260px}
.fcol-connect h5{margin-left:-15px}
.fcol-connect .inner{margin-left:-15px}
.circles{display:flex;gap:7px}
.circles span{width:23px;height:23px;border-radius:50%;background:#8ea6ab}
.fcol-connect p{color:#e6eeef;font-size:8.5px;line-height:10.5px;margin-top:10px}
.fcol-connect .field{width:150px;margin-top:6px;border-radius:11px;font-weight:normal}
.sub{color:#e6eeef;font-size:8.5px;font-weight:bold;margin-top:9px}
.fphone{display:flex;align-items:center;gap:8px;font-family:'Oswald',sans-serif;font-weight:300;font-size:21px;color:#b9cbce;margin-top:14px}
</style>
</head>
<body>
<header class="site-header">
  <div class="brand"><span class="brand-mark"></span><span class="brand-name">VOLTEN ELECTRICAL</span></div>
  <div class="social-top"><p><b>connect</b><br>with us on mingleton</p><span class="sq"></span></div>
</header>
<nav class="main-nav"><a href="#">Home</a><a href="#">About us</a><a href="#">Services</a><a href="#">Gallery</a><a href="#">Contact us</a></nav>
<section class="hero" role="img" aria-label="Two electricians in orange hard hats wiring a distribution panel">
  <div class="dots"><span></span><span></span><span></span><span></span><span></span></div>
</section>
<div class="fade"></div>

<main class="content">
  <div class="primary">
    <h1>WHY VOLTEN ELECTRICAL?</h1>
    <p class="intro">Lorem ipsum dolor sit amet, consectetur adipisicing elit, sed do eiusmod tempor incididunt ut labore et dolore magna aliqua. Ut enim ad minim veniam, quis nostrud exercitation ullamco laboris nisi ut aliquip ex ea commodo consequat. Duis aute irure dolor in reprehenderit in voluptate velit esse cillum dolore eu fugiat nulla pariatur. Excepteur sint occaecat cupidatat non proident, sunt in culpa qui officia deserunt mollit anim id est laborum.</p>
    <h2>WE USE ENERGY SAVING SOLUTIONS</h2>
    <div class="energy">
      <div class="art" role="img" aria-label="Green energy-saving light bulbs with leaves growing inside"></div>
      <div class="copy">
        <p>With the ever rising costs of energy, the need for each of us to make an effort to reduce our carbon foot-print and reduce our dependence on natural resources it is more important than ever for us all to "Go Green".</p>
        <ul>
          <li>Energy solution cost reduction and energy conservation</li>
          <li>Lighting retro, high performance LED &amp; CPFL's</li>
          <li>Net metering &amp; off grid energy solutions</li>
          <li>Electric Car Charging Solutions</li>
        </ul>
      </div>
    </div>
    <h3>WE DO SERVICE WITH THE FOLLOWING:</h3>
    <div class="services"><span>RESIDENTIAL</span><span>COMMERCIAL</span><span>CONSTRUCTION</span><span>INDUSTRIAL</span></div>
  </div>

  <aside class="aside">
    <h4>TESTIMONIALS</h4>
    <div class="quote">
      <svg class="bubble" viewBox="0 0 40 28"><ellipse cx="20" cy="12" rx="17" ry="10" fill="#7a9ca3"/><path d="M10 19 L7 27 L17 21Z" fill="#7a9ca3"/></svg>
      They are very professional and thrustworthy. No need for supervision while they are installing on work. It's been a while now and my electrical linings doesn't give me any problem. I highly recommend volten electrical.
      <cite>by: Dana Whitlow</cite>
    </div>
    <div class="quote">
      <svg class="bubble" viewBox="0 0 40 28"><ellipse cx="20" cy="12" rx="17" ry="10" fill="#7a9ca3"/><path d="M10 19 L7 27 L17 21Z" fill="#7a9ca3"/></svg>
      They are very professional and thrustworthy. No need for supervision while they are installing on work. It's been a while now and my electrical linings doesn't give me any problem. I highly recommend volten electrical.
      <cite>by: Dana Whitlow</cite>
    </div>
    <div class="call">
      <svg width="22" height="22" viewBox="0 0 22 22"><circle cx="11" cy="11" r="10" fill="none" stroke="#0c2e35" stroke-width="1.3"/><path d="M7.5 6c1-.6 1.6 0 2 1l.6 1.5c.2.6-.4 1-.8 1.3.5 1.3 1.4 2.3 2.7 2.9.4-.4.8-.9 1.4-.7l1.5.6c.9.4 1.5 1 .9 2-1 1.5-3 1.5-5.2-.3S6 7.4 7.5 6z" fill="#0c2e35"/></svg>
      CONTACT US NOW
    </div>
    <div class="phone-big">0-21-55501234</div>
  </aside>
</main>

<footer class="site-footer">
  <div class="fcol-nav">
    <h5>NAVIGATION</h5>
    <a href="#">Home</a><a href="#">About Us</a><a href="#">Services</a><a href="#">Gallery</a><a href="#">Contact Us</a>
  </div>
  <div class="fcol-mail">
    <h5>EMAIL US</h5>
    <div class="field">full name</div>
    <div class="field">email address</div>
    <div class="field area"></div>
    <span class="send">send</span>
  </div>
  <div class="fcol-connect">
    <h5>CONNECT WITH US</h5>
    <div class="inner">
      <div class="circles"><span></span><span></span><span></span><span></span><span></span></div>
      <p>subscribe to our monthly newsletter<br>and get the best deals and discounts</p>
      <div class="field">enter email address</div>
      <div class="sub">&#10148;&nbsp; subscribe now</div>
      <div class="fphone">
        <svg width="22" height="22" viewBox="0 0 22 22"><circle cx="11" cy="11" r="10" fill="none" stroke="#b9cbce" stroke-width="1.3"/><path d="M7.5 6c1-.6 1.6 0 2 1l.6 1.5c.2.6-.4 1-.8 1.3.5 1.3 1.4 2.3 2.7 2.9.4-.4.8-.9 1.4-.7l1.5.6c.9.4 1.5 1 .9 2-1 1.5-3 1.5-5.2-.3S6 7.4 7.5 6z" fill="#b9cbce"/></svg>
        0-21-5550123
      </div>
    </div>
  </div>
</footer>
</body>
</html>
```